Veltrano - Mechanic/Collision Center Business Card

We're looking for a business card design for our mechanic/ collision repair shop.

Can be with colours or monochromatic.

See the attached files.

Many thanks

```html
<!DOCTYPE html>
<html lang="pt">
<head>
<meta charset="utf-8">
<title>Veltrano – Business Card</title>
<link href="https://fonts.googleapis.com/css2?family=Roboto:wght@400;500;900&display=swap" rel="stylesheet">
<style>
  :root {
    --stage: #9a9ea3;
    --card: #ffffff;
    --ink: #1d2023;
    --grey: #5b5e62;
    --blue: #1b9ad6;
    --edge-blue: #a9d7ef;
    --edge-grey: #55585c;
  }
  * { box-sizing: border-box; margin: 0; padding: 0; }
  html, body { width: 1200px; height: 913px; overflow: hidden; }
  body {
    background: var(--stage);
    font-family: "Roboto", sans-serif;
    position: relative;
  }
  .card {
    position: absolute;
    width: 560px;
    height: 320px;
    background: var(--card);
    border-radius: 16px;
    box-shadow: 0 6px 0 var(--edge-blue), 0 14px 26px rgba(0,0,0,.25);
    overflow: hidden;
  }
  .card--front { left: 60px; top: 80px; }
  .card--back  { left: 580px; top: 500px; box-shadow: 0 6px 0 var(--edge-grey), 0 14px 26px rgba(0,0,0,.25); }

  .brand {
    display: flex;
    align-items: center;
    gap: 16px;
  }
  .brand__dot {
    width: 44px; height: 44px;
    border-radius: 50%;
    background: var(--blue);
    flex: none;
  }
  .brand__name {
    font-weight: 900;
    color: var(--ink);
    letter-spacing: 1px;
    text-transform: uppercase;
  }
  .card--front .brand {
    position: absolute;
    inset: 0;
    justify-content: center;
  }
  .card--front .brand__name { font-size: 58px; }

  .card--back .brand {
    position: absolute;
    left: 40px; top: 0; bottom: 0;
    width: 240px;
    justify-content: center;
  }
  .card--back .brand__dot { width: 30px; height: 30px; }
  .card--back .brand__name { font-size: 32px; }

  .divider {
    position: absolute;
    left: 300px; top: 70px;
    width: 1.5px; height: 190px;
    background: var(--blue);
  }
  .details {
    position: absolute;
    left: 322px; top: 34px; right: 20px;
    color: var(--grey);
    font-size: 14px;
    line-height: 1.4;
  }
  .person { text-align: right; margin-bottom: 42px; }
  .person__name { color: var(--blue); font-size: 22px; font-weight: 400; letter-spacing: .5px; }
  .person__role { font-size: 11px; letter-spacing: 1px; margin-top: -2px; }
  .company { color: var(--blue); font-weight: 500; }
  .contact { list-style: none; margin-top: 2px; }
  .contact li { display: flex; align-items: center; gap: 8px; }
  .contact svg { width: 13px; height: 13px; flex: none; fill: var(--blue); }
</style>
</head>
<body>

<section class="card card--front" aria-label="Card front">
  <div class="brand">
    <span class="brand__dot"></span>
    <span class="brand__name">Veltrano</span>
  </div>
</section>

<section class="card card--back" aria-label="Card back">
  <div class="brand">
    <span class="brand__dot"></span>
    <span class="brand__name">Veltrano</span>
  </div>

  <div class="divider"></div>

  <div class="details">
    <div class="person">
      <div class="person__name">RUI MATOS</div>
      <div class="person__role">MANAGER</div>
    </div>
    <div class="company">Veltrano, LDA</div>
    <div>Rua das Oficinas, 42</div>
    <div>1900-214 Lisboa</div>
    <ul class="contact">
      <li>
        <svg viewBox="0 0 16 16" aria-hidden="true"><path d="M3 1h3l1.5 4-2 1.3a9 9 0 0 0 4.2 4.2L11 8.5l4 1.5v3a2 2 0 0 1-2 2C6.4 15 1 9.6 1 3a2 2 0 0 1 2-2z"/></svg>
        +351 912000555
      </li>
      <li>
        <svg viewBox="0 0 16 16" aria-hidden="true"><path d="M1 3h14v10H1z M1 3l7 6 7-6" fill="none" stroke="#1b9ad6" stroke-width="1.6"/></svg>
        veltrano.oficina@mail.pt
      </li>
      <li>
        <svg viewBox="0 0 16 16" aria-hidden="true"><rect x="1" y="1" width="14" height="14" rx="2"/></svg>
        social.veltrano.pt
      </li>
    </ul>
  </div>
</section>

</body>
</html>
```